Dyslexia Assessment Business card design

we need a business card design for a new company based in New Hampshire called Bright Paths Learning Center. We provide dyslexia assessment and consultation
Updates

Can you please add my degrees/certifications Carla Dunmore MA, MEd NH Certified Specialist in the Assessment of Intellectual Functioning Reading and Writing Specialist Learning Disabilities Specialist

I am interested in also creating a web page. If you have experience with webpages that may be useful. I have the domains but am waiting the name of the business to be cleared by the state. I expect this to take place within the month.

I think listing all the certifications is too much. Please just add Carla Dunmore MA, MEd, SAIF

Target Market(s)

parents of kids with dyslexia

Industry/Entity Type

Business

Contact Information for Business Card

Bright Paths Learning Center
Carla Dunmore - Dyslexia Diagnostician/Consultant
42 Fenwick Lane Londonderry, NH 03071
Phone (603)418-2275
WWW.BrightPathsLearningCenter.com
BrightPathsLearningCenter@mailbox-example.com

Requirements
Nice to have
• can have 2 sides not essential though

maybe "dyslexia" in the background spelled wrong or letters backward

```html
<!DOCTYPE html>
<html lang="en">
<head>
<meta charset="utf-8">
<title>Bright Paths Learning Center – Business Card</title>
<link rel="stylesheet" href="https://fonts.googleapis.com/css2?family=Lora:wght@400;500;600&display=swap">
<style>
  :root {
    --page-bg: #dcd7cf;
    --card-bg: #eef0ee;
    --ink: #1c1c1c;
    --watermark: #8f8a84;
    --band-green: #5a9a35;
    --band-blue: #2b5aa6;
    --band-blue-deep: #1f4d96;
    --band-text: #ece6d4;
    --band-text-soft: #d9d6cf;
    --mark: #2c5a9c;
  }
  * { margin: 0; padding: 0; box-sizing: border-box; }
  html, body { width: 1200px; height: 1200px; overflow: hidden; }
  body {
    background: var(--page-bg);
    font-family: "Lora", Georgia, serif;
    position: relative;
  }
  .card {
    position: absolute;
    left: 60px; top: 268px;
    width: 1080px; height: 665px;
    background: var(--card-bg);
    border-radius: 24px;
    overflow: hidden;
    box-shadow: 0 6px 24px rgba(0,0,0,0.12);
  }
  .brand-mark {
    position: absolute;
    left: 40px; top: 92px;
    width: 190px; height: 190px;
    background: var(--mark);
  }
  .brand-name {
    position: absolute;
    left: 268px; top: 62px;
    font-size: 70px;
    line-height: 76px;
    font-weight: 500;
    color: var(--ink);
  }
  .watermark-word {
    position: absolute;
    right: 6px; top: 248px;
    font-size: 104px;
    line-height: 1;
    color: var(--watermark);
    opacity: 0.75;
  }
  .address-band {
    position: absolute;
    left: 0; top: 381px;
    width: 100%; height: 47px;
    background: var(--band-green);
    color: var(--band-text);
    font-size: 25px;
    font-weight: 600;
    line-height: 47px;
    padding-left: 18px;
    white-space: nowrap;
  }
  .contact-band {
    position: absolute;
    left: 0; top: 428px;
    width: 100%; height: 163px;
    background: linear-gradient(180deg, var(--band-blue) 0%, var(--band-blue-deep) 100%);
    color: var(--band-text);
  }
  .person { position: absolute; left: 18px; top: 22px; white-space: nowrap; }
  .person-name { font-size: 38px; font-weight: 600; line-height: 48px; }
  .person-creds { font-size: 24px; font-weight: 500; line-height: 32px; }
  .person-title { font-size: 23px; line-height: 32px; color: var(--band-text-soft); }
  .contact-list { position: absolute; left: 470px; top: 24px; list-style: none; }
  .contact-list li {
    display: flex; align-items: center;
    font-size: 21px; line-height: 36px;
    white-space: nowrap;
  }
  .contact-list li.phone { font-size: 29px; font-weight: 500; line-height: 40px; }
  .contact-list svg { width: 24px; height: 24px; margin-right: 18px; flex: none; }
</style>
</head>
<body>
  <div class="card">
    <div class="brand-mark"></div>
    <div class="brand-name">Bright Paths<br>Learning<br>Center</div>
    <div class="watermark-word">Dyslexia</div>

    <div class="address-band">42 Fenwick Lane Londonderry, NH 03071</div>

    <div class="contact-band">
      <div class="person">
        <div class="person-name">Carla Dunmore</div>
        <div class="person-creds">MA, MEd, SAIF</div>
        <div class="person-title">Dyslexia Diagnostician/Consultant</div>
      </div>
      <ul class="contact-list">
        <li class="phone">
          <svg viewBox="0 0 24 24" fill="currentColor"><path d="M3 9c0-3 4-5 9-5s9 2 9 5v2h-5V9H8v2H3z"/><rect x="5" y="12" width="14" height="8" rx="2"/><circle cx="12" cy="16" r="2" fill="var(--band-blue)"/></svg>
          (603)418-2275
        </li>
        <li>
          <svg viewBox="0 0 24 24" fill="currentColor"><path d="M2 5h20v14H2z"/><path d="M2 5l10 8 10-8" fill="none" stroke="var(--band-blue)" stroke-width="1.8"/></svg>
          BrightPathsLearningCenter@mailbox-example.com
        </li>
        <li>
          <svg viewBox="0 0 24 24" fill="none" stroke="currentColor" stroke-width="1.6"><circle cx="12" cy="12" r="9"/><ellipse cx="12" cy="12" rx="4" ry="9"/><path d="M3 12h18M5 7h14M5 17h14"/></svg>
          www.BrightPathsLearningCenter.com
        </li>
      </ul>
    </div>
  </div>
</body>
</html>
```